Help a start up law firm make an impression! - Website

We are a property development and conveyancing law firm looking for some to design our website. The initial brief is for 6 pages with scope for on-going work.

Law firms are traditionally quite conservative and we want to break the mold. We want to come across as fun and modern, while still being professional.

A good example is https://quorvantlaw.com.au/. It's professional yet modern.
Updates

Another good site I like in the same industry: https://www.tamberwickconveyancing.com.au/

Target Market(s)

Tech savy home buyers and sellers - generally 30 to 50 years old

Industry/Entity Type

Law Firm

Coding

Coded - Design and coding required

Number of Pages Required

5+ page

Font styles to use
Other font styles liked:
• No idea

Colors
f04a50

Requirements
Must have
• The elements set out in the design brief document

```html
<!DOCTYPE html>
<html lang="en">
<head>
<meta charset="utf-8">
<title>Brennock Law</title>
<link href="https://fonts.googleapis.com/css2?family=Montserrat:wght@400;600;700;800&family=Open+Sans:wght@400;600&display=swap" rel="stylesheet">
<style>
:root{
  --pink:#e04a5f;
  --pink-dark:#c93a4f;
  --ink:#2b2b2b;
  --text:#555;
  --muted:#8a8a8a;
  --dark:#4a4a4a;
  --darker:#3c3c3c;
  --light:#f1f1f1;
  --line:#d9d9d9;
  --white:#fff;
}
*{box-sizing:border-box;margin:0;padding:0}
html,body{width:1200px;height:4100px;overflow:hidden}
body{position:relative;background:var(--white);font-family:"Open Sans",Arial,sans-serif;color:var(--text);font-size:15px}
.abs{position:absolute}
h1,h2,h3,h4,.heading{font-family:"Montserrat",Arial,sans-serif}

/* header */
.topbar{left:0;top:0;width:1200px;height:112px;background:var(--white)}
.brand{left:64px;top:30px;font-family:"Montserrat",sans-serif;font-weight:800;font-size:44px;color:var(--pink);letter-spacing:-1px}
.social{top:34px;display:flex;gap:14px;left:770px}
.social span{width:34px;height:34px;border-radius:50%;background:var(--dark);display:block}
.phone{left:960px;top:30px;color:var(--pink);font-family:"Montserrat",sans-serif}
.phone small{display:block;font-size:11px;color:var(--muted);letter-spacing:1px}
.phone b{font-size:24px;font-weight:700}
.phone-icon{position:absolute;left:-34px;top:16px}
.nav{left:0;top:112px;width:1200px;height:38px;background:var(--pink);display:flex;align-items:center;padding-left:100px;gap:58px}
.nav a{color:var(--white);text-decoration:none;font-family:"Montserrat",sans-serif;font-size:13px;font-weight:600;letter-spacing:.5px}

/* hero */
.hero{left:0;top:150px;width:1200px;height:590px;background:linear-gradient(120deg,#3a3838 0%,#6b6764 35%,#c9c4bd 55%,#8d8782 80%,#4a4644 100%);clip-path:polygon(0 0,100% 0,100% 78%,0 100%)}
.hero-card{left:700px;top:290px;width:400px;background:rgba(30,30,30,.78);padding:28px 30px 30px}
.hero-card h1{color:var(--white);font-size:26px;font-weight:700;line-height:1.3;text-transform:uppercase}
.btn{display:inline-block;font-family:"Montserrat",sans-serif;font-weight:600;font-size:13px;text-transform:uppercase;text-decoration:none}
.btn-pink{background:var(--pink);color:var(--white);padding:9px 22px;margin-top:16px}

/* about */
.about{left:100px;top:850px;width:620px}
.section-title{font-size:30px;font-weight:700;color:var(--ink);text-transform:uppercase}
.about .underline{width:110px;height:4px;background:var(--pink);margin:12px 0 24px}
.adv{display:flex;gap:22px}
.adv-photo{width:120px;height:84px;background:linear-gradient(135deg,#6a5d55,#b8aa9c);flex:none}
.adv h4{color:var(--pink);font-size:14px;font-weight:700;margin-bottom:6px}
.adv p,.about p{font-size:14px;line-height:1.6;color:var(--muted)}
.about > p{margin-top:20px}
.readmore{color:var(--pink);font-weight:600;font-size:14px;margin-top:14px;display:block;text-decoration:none}

.ask{left:780px;top:770px;width:320px;height:350px;background:var(--pink);padding:28px 26px}
.ask h2{color:var(--white);font-size:27px;font-weight:700;text-transform:uppercase;margin-bottom:18px}
.field{background:var(--white);height:40px;margin-bottom:14px;padding:11px 14px;font-size:13px;color:#999}
.btn-dark{background:var(--ink);color:var(--white);padding:13px;width:100%;text-align:center;margin-top:4px;font-size:14px}

/* services */
.services{left:0;top:1200px;width:1200px;height:660px;background:var(--dark);clip-path:polygon(0 12%,100% 0,100% 100%,0 100%)}
.section-head{width:1200px;left:0;text-align:center}
.section-head h2{font-size:30px;font-weight:700;text-transform:uppercase}
.divider{display:flex;align-items:center;justify-content:center;gap:14px;margin-top:16px}
.divider i{display:block;width:230px;height:1px;background:currentColor;opacity:.5}
.light{color:var(--white)}
.darkhead{color:var(--ink)}
.service{width:240px;text-align:center;color:var(--white)}
.service .ring{width:110px;height:110px;border-radius:50%;background:var(--pink);margin:0 auto;display:flex;align-items:center;justify-content:center;border:6px solid rgba(255,255,255,.15)}
.service h3{font-size:16px;font-weight:700;margin:26px 0 12px;text-transform:uppercase}
.service p{font-size:13px;line-height:1.6;color:#d8d8d8}
.btn-outline{border:1px solid var(--white);color:var(--white);padding:6px 16px;margin-top:16px;font-size:12px;text-transform:none}

/* news */
.news{top:2020px;width:480px;height:300px;display:flex;background:var(--light)}
.news-text{width:50%;padding:40px 22px}
.news-text h4{color:var(--pink);font-size:14px;font-weight:700;margin-bottom:12px}
.news-text p{font-size:13px;line-height:1.6;color:var(--muted)}
.news-text a{display:block;margin-top:14px;font-size:13px;color:var(--ink);text-decoration:none;font-weight:600}
.news-photo{width:50%;position:relative}
.date-tag{position:absolute;top:0;width:70px;height:70px;background:var(--dark);color:var(--white);font-family:"Montserrat",sans-serif;font-size:13px;text-align:center;padding-top:16px;line-height:1.3}
.dots{top:2405px;left:570px;display:flex;gap:14px}
.dots span{width:14px;height:14px;border-radius:50%;background:#c7c7c7}
.dots span:first-child{background:var(--pink)}

/* get in touch */
.touch{left:0;top:2540px;width:1200px;height:490px;background:var(--light);clip-path:polygon(0 22%,50% 0,100% 22%,100% 100%,0 100%)}
.touch-sub{top:2750px;left:0;width:1200px;text-align:center;font-size:15px;color:var(--text)}
.tfield{background:var(--white);height:44px;border:1px solid #e2e2e2;padding:12px 14px;font-size:13px;color:#999}
.btn-submit{left:510px;top:2960px;width:180px;background:var(--pink);color:var(--white);text-align:center;padding:13px 0;font-size:14px}

/* map */
.map{left:0;top:3030px;width:1200px;height:340px;background:linear-gradient(180deg,#dcdcdc,#c9c9c9 60%,#d8d3d5)}

/* contact */
.contact{left:0;top:3330px;width:1200px;height:720px;background:var(--darker);clip-path:polygon(0 12%,50% 0,100% 12%,100% 100%,0 100%)}
.contact-form{left:130px;top:3630px;width:410px;height:370px;background:var(--light);padding:24px}
.contact-form h3{font-size:20px;font-weight:600;color:var(--ink);margin-bottom:18px}
.cf{background:var(--white);height:40px;margin-bottom:14px;padding:11px 14px;font-size:13px;color:#999}
.btn-send{float:right;background:var(--pink);color:var(--white);padding:9px 22px;font-size:12px}
.company{left:600px;top:3640px;color:var(--white);font-size:24px;font-weight:700}
.info{color:var(--white);width:260px}
.info h4{font-size:18px;font-weight:700;margin-bottom:14px}
.info p{font-size:13px;line-height:1.6;color:#cfcfcf;padding-left:34px;position:relative}
.info svg{position:absolute;left:0;top:2px}
.footer{left:0;top:4050px;width:1200px;height:50px;background:var(--pink);color:var(--white);text-align:center;font-size:13px;padding-top:16px}
</style>
</head>
<body>

<header class="abs topbar">
  <div class="abs brand">Brennock Law</div>
  <div class="abs social" aria-label="Social links"><span></span><span></span><span></span></div>
  <div class="abs phone">
    <svg class="phone-icon" width="22" height="22" viewBox="0 0 24 24"><path fill="#e04a5f" d="M6.6 10.8a15.1 15.1 0 0 0 6.6 6.6l2.2-2.2c.3-.3.7-.4 1-.2 1.1.4 2.3.6 3.6.6.6 0 1 .4 1 1V20c0 .6-.4 1-1 1A17 17 0 0 1 3 4c0-.6.4-1 1-1h3.5c.6 0 1 .4 1 1 0 1.3.2 2.5.6 3.6.1.3 0 .7-.2 1z"/></svg>
    <small>CALL US NOW</small><b>1.800.555.0142</b>
  </div>
</header>
<nav class="abs nav">
  <a href="#">HOME</a><a href="#">CONVEYANCING</a><a href="#">PROPERTY DEVELOPMENT</a><a href="#">NEWS &amp; KNOWLEDGE</a><a href="#">ABOUT US</a><a href="#">CONTACT US</a>
</nav>

<section class="abs hero" role="img" aria-label="Photo of a person at a desk holding a phone beside documents and a coffee cup"></section>
<div class="abs hero-card">
  <h1>At Brennock Law, you are our first priority</h1>
  <a class="btn btn-pink" href="#">Read more</a>
</div>

<section class="abs about">
  <h2 class="section-title">About Brennock Law</h2>
  <div class="underline"></div>
  <div class="adv">
    <div class="adv-photo" role="img" aria-label="Photo of a client meeting"></div>
    <div>
      <h4>WHAT ARE OUR ADVANTAGES?</h4>
      <p>What does your property deal need to succeed? We explain each step and help you solve a problem fast.</p>
    </div>
  </div>
  <p>We guide buyers and sellers through every stage of a property transfer with clear advice, fixed fees and fast replies. Our team explains the fine print so you can sign with confidence and move on with your plans.</p>
  <a class="readmore" href="#">Read More &rsaquo;</a>
</section>

<aside class="abs ask">
  <h2>Have a question?</h2>
  <div class="field">Your Name</div>
  <div class="field">Your Email</div>
  <div class="field">Phone No.</div>
  <div class="btn btn-dark">Get started</div>
</aside>

<section class="abs services"></section>
<div class="abs section-head light" style="top:1340px">
  <h2>Our Services</h2>
  <div class="divider"><i></i><svg width="22" height="22" viewBox="0 0 22 22"><rect x="6" y="6" width="10" height="10" transform="rotate(45 11 11)" fill="#fff"/></svg><i></i></div>
</div>

<div class="abs service" style="left:100px;top:1460px">
  <div class="ring"><svg width="50" height="50" viewBox="0 0 24 24" fill="none" stroke="#fff" stroke-width="2"><circle cx="12" cy="12" r="9"/><path d="M12 7v10M9 9.5c0-1.2 1.3-2 3-2s3 .8 3 2-1.3 1.8-3 2.2-3 1-3 2.3 1.3 2 3 2 3-.8 3-2"/></svg></div>
  <h3>Cost certainty</h3>
  <p>Clear fixed pricing on every matter, so you know the full cost of your property deal from day one.</p>
  <a class="btn btn-outline" href="#">Read more &rsaquo;</a>
</div>
<div class="abs service" style="left:370px;top:1460px">
  <div class="ring"><svg width="54" height="54" viewBox="0 0 24 24" fill="#fff"><circle cx="8" cy="8" r="3"/><circle cx="16" cy="8" r="3"/><path d="M2 19c0-3.3 2.7-6 6-6s6 2.7 6 6zM12 19c0-2 1-3.8 2.5-5 .5-.1 1-.1 1.5-.1 3.3 0 6 2.7 6 5.1z"/></svg></div>
  <h3>Expert lawyers</h3>
  <p>Our property lawyers bring years of hands on practice to each sale, purchase and development file.</p>
  <a class="btn btn-outline" href="#">Read more &rsaquo;</a>
</div>
<div class="abs service" style="left:640px;top:1460px">
  <div class="ring"><svg width="50" height="50" viewBox="0 0 24 24" fill="#fff"><circle cx="12" cy="8" r="4"/><path d="M4 21c0-4.4 3.6-8 8-8s8 3.6 8 8z"/></svg></div>
  <h3>Responsive service</h3>
  <p>Reach your lawyer by phone, email or chat and get a real answer the same business day.</p>
  <a class="btn btn-outline" href="#">Read more &rsaquo;</a>
</div>
<div class="abs service" style="left:910px;top:1460px">
  <div class="ring"><svg width="50" height="50" viewBox="0 0 24 24" fill="none" stroke="#fff" stroke-width="2"><rect x="5" y="3" width="14" height="18" rx="1"/><path d="M8 8h8M8 12h8M8 16h5"/></svg></div>
  <h3>Commercial advice</h3>
  <p>Practical guidance for developers on land deals, contracts and staged projects of every size.</p>
  <a class="btn btn-outline" href="#">Read more &rsaquo;</a>
</div>

<div class="abs section-head darkhead" style="top:1930px">
  <h2>Knowledge and news</h2>
  <div class="divider"><i></i><svg width="22" height="22" viewBox="0 0 22 22"><rect x="6" y="6" width="10" height="10" transform="rotate(45 11 11)" fill="#2b2b2b"/></svg><i></i></div>
</div>

<article class="abs news" style="left:100px">
  <div class="news-text">
    <h4>Real estate laws on the move</h4>
    <p>New rules for buyers take effect this year. Here is what they mean for your next purchase.</p>
    <a href="#">Read More &rsaquo;</a>
  </div>
  <div class="news-photo" role="img" aria-label="Photo looking up at city office towers" style="background:linear-gradient(180deg,#5c6b78,#2f3a44)">
    <div class="date-tag" style="left:0">12<br>JAN</div>
  </div>
</article>
<article class="abs news" style="left:620px">
  <div class="news-text">
    <h4>Real estate laws on the move</h4>
    <p>Changes to settlement timelines could affect sellers. Our team explains the key points.</p>
    <a href="#">Read More &rsaquo;</a>
  </div>
  <div class="news-photo" role="img" aria-label="Photo of two business people in suits in an office" style="background:linear-gradient(180deg,#c9d3dc,#3c4248)">
    <div class="date-tag" style="left:0">08<br>FEB</div>
  </div>
</article>
<div class="abs dots"><span></span><span></span><span></span></div>

<section class="abs touch"></section>
<div class="abs section-head darkhead" style="top:2660px">
  <h2>Get in touch</h2>
  <div class="divider"><i></i><svg width="22" height="22" viewBox="0 0 22 22"><rect x="6" y="6" width="10" height="10" transform="rotate(45 11 11)" fill="#2b2b2b"/></svg><i></i></div>
</div>
<p class="abs touch-sub">Fill out the form below to get in touch. A team member will be in touch shortly!</p>
<div class="abs tfield" style="left:130px;top:2800px;width:440px">Full Name</div>
<div class="abs tfield" style="left:130px;top:2856px;width:440px">Email Address</div>
<div class="abs tfield" style="left:130px;top:2912px;width:440px">Phone Number</div>
<div class="abs tfield" style="left:620px;top:2800px;width:440px;height:156px">Your Message</div>
<div class="abs btn btn-submit">Submit</div>

<section class="abs map" role="img" aria-label="Street map showing the office location"></section>
<svg class="abs" style="left:488px;top:3160px" width="44" height="60" viewBox="0 0 24 32"><path fill="#e04a5f" d="M12 0C5.4 0 0 5.4 0 12c0 9 12 20 12 20s12-11 12-20C24 5.4 18.6 0 12 0z"/><circle cx="12" cy="12" r="5" fill="#fff"/></svg>

<section class="abs contact"></section>
<div class="abs section-head light" style="top:3490px">
  <h2>Contact us</h2>
  <div class="divider"><i></i><svg width="22" height="22" viewBox="0 0 22 22"><rect x="6" y="6" width="10" height="10" transform="rotate(45 11 11)" fill="#fff"/></svg><i></i></div>
</div>

<div class="abs contact-form">
  <h3>Contact form</h3>
  <div class="cf">Name</div>
  <div class="cf">Email</div>
  <div class="cf" style="height:120px">Message</div>
  <div class="btn btn-send">Submit</div>
</div>

<h3 class="abs company">A Full Service Technology Company.</h3>
<div class="abs info" style="left:600px;top:3700px">
  <h4>Address</h4>
  <p><svg width="20" height="20" viewBox="0 0 24 24"><path fill="#e04a5f" d="M12 2a7 7 0 0 0-7 7c0 5 7 13 7 13s7-8 7-13a7 7 0 0 0-7-7zm0 9.5A2.5 2.5 0 1 1 12 6.5a2.5 2.5 0 0 1 0 5z"/></svg>Brennock Law Head Office<br>48 Harbour Lane<br>Newtown, NY 10021</p>
</div>
<div class="abs info" style="left:880px;top:3700px">
  <h4>Phone</h4>
  <p><svg width="20" height="20" viewBox="0 0 24 24"><path fill="#e04a5f" d="M12 2a7 7 0 0 0-7 7c0 5 7 13 7 13s7-8 7-13a7 7 0 0 0-7-7zm0 9.5A2.5 2.5 0 1 1 12 6.5a2.5 2.5 0 0 1 0 5z"/></svg>210 Larchmont Place<br>Suite 14<br>Fairview, CA 90210</p>
</div>
<div class="abs info" style="left:600px;top:3860px">
  <h4>Business Hours</h4>
  <p><svg width="20" height="20" viewBox="0 0 24 24" fill="none" stroke="#e04a5f" stroke-width="2"><circle cx="12" cy="12" r="9"/><path d="M12 7v5l3 2"/></svg>Monday-Friday : 9am - 6pm<br>Saturday : 10am - 4pm<br>Sunday : Closed</p>
</div>
<div class="abs info" style="left:880px;top:3860px">
  <h4>Business Hours</h4>
  <p><svg width="20" height="20" viewBox="0 0 24 24" fill="none" stroke="#e04a5f" stroke-width="2"><rect x="3" y="5" width="18" height="14" rx="1"/><path d="M3 6l9 7 9-7"/></svg>hello@brennocklaw.example<br>1.800.555.0142<br>office@brennocklaw.example</p>
</div>

<footer class="abs footer">&copy; Copyright - 2017 &nbsp;|&nbsp; All Rights Reserved</footer>

</body>
</html>
```